Looking for a Micropage Template

My website will be offering our users to have their very own micropage / profile page hosted on our website.

I am looking for someone to design a a web micropage / profile template that matches the color theme of our websites homepage.

1. Follow the colors of our homepage

2. Open the excel sheet and follow the directions to design a micropage / profile page template.

Target Market(s)

Travel Market

Industry/Entity Type

Travel

Number of Pages Required

1 page

Requirements
Must have
• All of the fields specified in the excel sheet
Nice to have
• Follow the color themes and style of the company homepage
• Different color themes is acceptable as long as it looks nice
• Nice HQ photos

```html
<!DOCTYPE html>
<html lang="en">
<head>
<meta charset="utf-8">
<title>Guide Profile – New York</title>
<link href="https://fonts.googleapis.com/css2?family=Source+Sans+3:wght@400;600;700&display=swap" rel="stylesheet">
<style>
:root{
  --teal:#3bbbbd;
  --teal-dark:#2aa3a6;
  --hero-top:#9a8a3a;
  --hero-mid:#3e8f93;
  --hero-low:#16424f;
  --hero-base:#0f2e3a;
  --yellow:#f2c53d;
  --yellow-dark:#d3a72a;
  --white:#ffffff;
  --muted:#9a9a9a;
  --rule:#cfcfcf;
  --footer:#474747;
}
*{margin:0;padding:0;box-sizing:border-box}
html,body{width:854px;height:1200px;overflow:hidden}
body{font-family:"Source Sans 3",sans-serif;background:var(--white);position:relative;color:var(--white)}
.abs{position:absolute}

/* hero */
.hero{left:0;top:0;width:854px;height:334px;
  background:linear-gradient(180deg,var(--hero-top) 0%,#6f9063 22%,var(--hero-mid) 50%,var(--hero-low) 82%,var(--hero-base) 100%)}
.avatar{left:62px;top:17px;width:102px;height:102px;border-radius:50%;border:3px solid var(--yellow);
  background:linear-gradient(160deg,#d8dde0,#9aa4aa)}
.profile-line{left:61px;width:127px;font-size:11px;font-weight:600;padding:0 0 3px 10px;border-bottom:1px solid rgba(255,255,255,.45)}
.category{left:735px;top:18px;width:60px;height:60px;border-radius:50%;background:var(--white);border:3px solid var(--teal)}
.category svg{position:absolute;left:13px;top:13px}
.category-label{left:720px;top:83px;width:90px;text-align:center;font-size:8px;font-weight:700;letter-spacing:.2px}
.city{left:0;top:185px;width:922px;text-align:center;font-size:38px;font-weight:600;line-height:1}
.city span{display:inline-block;border-bottom:1px solid rgba(255,255,255,.5);padding-bottom:2px}
.rate{left:669px;top:298px;width:126px;font-size:10.5px;font-weight:600;padding:0 0 4px 10px;border-bottom:1px solid rgba(255,255,255,.45)}

/* about */
.about{left:0;top:334px;width:854px;height:213px;background:var(--teal)}
.notch{width:0;height:0;border-left:14px solid transparent;border-right:14px solid transparent}
.notch-hero{left:413px;top:334px;border-top:14px solid var(--hero-base)}
.notch-about{left:413px;top:547px;border-top:14px solid var(--teal)}
.notch-contact{left:413px;top:902px;border-top:14px solid var(--white)}
.bio{left:61px;top:360px;width:432px;font-size:9.4px;line-height:16.5px}
.bio p+p{margin-top:16.5px}
.feature{left:585px;height:38px;display:flex;align-items:center}
.feature-icon{width:38px;height:38px;border-radius:50%;background:var(--white);border:2px solid rgba(255,255,255,.6);box-shadow:0 0 0 2px var(--teal) inset;display:flex;align-items:center;justify-content:center}
.feature-label{margin-left:13px;font-size:10.5px}

/* contact */
.contact-title{left:0;top:600px;width:854px;text-align:center;color:var(--teal);font-size:29px;font-weight:700}
.field{left:61px;width:352px;height:22px;border-bottom:1px solid var(--rule);color:var(--muted);font-size:10.5px;padding-left:13px}
.field svg{position:absolute;right:0;top:0}
.message{left:443px;top:684px;width:352px;height:96px;border-bottom:1px solid var(--rule);color:var(--muted);font-size:10.5px;padding-left:13px}
.send{left:362px;top:824px;width:128px;height:36px;background:var(--yellow);border-bottom:3px solid var(--yellow-dark);border-radius:2px;color:var(--white);font-size:10.5px;font-weight:600;letter-spacing:.3px;display:flex;align-items:center;justify-content:center}

/* connect */
.connect{left:0;top:902px;width:854px;height:256px;background:var(--teal)}
.connect-title{left:0;top:944px;width:860px;text-align:center;font-size:29px;font-weight:700}
.network{top:1027px;width:57px;height:57px;border-radius:50%;background:var(--white);color:var(--teal);font-size:8.5px;font-weight:600;display:flex;align-items:center;justify-content:center}

/* footer */
.footer{left:0;top:1158px;width:854px;height:42px;background:var(--footer);font-size:6.8px;display:flex;align-items:center;justify-content:space-between;padding:0 59px 0 61px}
</style>
</head>
<body>

<section class="abs hero" role="img" aria-label="City skyline photograph of a waterfront with high-rise towers under a teal and olive tint"></section>
<div class="abs avatar" role="img" aria-label="Portrait photo of the guide"></div>
<div class="abs profile-line" style="top:129px">John Doe</div>
<div class="abs profile-line" style="top:155px">https://wayfarepage.com</div>

<div class="abs category">
  <svg width="28" height="28" viewBox="0 0 28 28" fill="none" stroke="#3bbbbd" stroke-width="3" stroke-linecap="round">
    <line x1="4" y1="24" x2="22" y2="5"/><line x1="6" y1="5" x2="24" y2="24"/><line x1="18" y1="3" x2="25" y2="10" stroke-width="2"/>
  </svg>
</div>
<div class="abs category-label">RESTAURANT</div>

<h1 class="abs city"><span>New York, United States</span></h1>
<div class="abs rate">$35 / Per Hour</div>

<section class="abs about"></section>
<div class="abs notch notch-hero"></div>
<div class="abs bio">
  <p>Lorem ipsum dolor sit amet consecutor. Lorem ipsum dolor sit amet consecutor. Lorem ipsum dolor sit amet consecutor. Lorem ipsum dolor sit amet consecutor. Lorem ipsum dolor sit amet consecutor. Lorem ipsum dolor sit amet consecutor. Lorem ipsum dolor sit amet consecutor. Lorem ipsum dolor sit amet consecutor. Lorem ipsum dolor sit amet consecutor. Loremipsum dolor sit amet consecutor.</p>
  <p>Lorem ipsum dolor sit amet consecutor. Lorem ipsum dolor sit amet consecutor. Lorem ipsum dolor sit amet consecutor. Lorem ipsum dolor sit amet consecutor. Lorem ipsum dolor sit amet consecutor. Lorem ipsum dolor sit amet consecutor. Lorem ipsum dolor sit amet consecutor. Lorem ipsum dolor sit amet consecutor. Lorem ipsum dolor sit amet consecutor. Lorem ipsum dolor sit amet consecutor.</p>
</div>

<div class="abs feature" style="top:345px">
  <div class="feature-icon"><svg width="18" height="18" viewBox="0 0 18 18" fill="none" stroke="#f2c53d" stroke-width="1.6"><circle cx="9" cy="9" r="6"/><path d="M3 9h12M9 3c-3 3-3 9 0 12M9 3c3 3 3 9 0 12"/></svg></div>
  <span class="feature-label">Speaks Mandarin</span>
</div>
<div class="abs feature" style="top:393px">
  <div class="feature-icon"><svg width="18" height="18" viewBox="0 0 18 18" fill="none" stroke="#f2c53d" stroke-width="1.6"><path d="M2 9h14c0 4-3 6-7 6s-7-2-7-6z" fill="#f2c53d"/><path d="M10 7c0-2 2-2 2-4M13 7c0-2 2-2 2-4"/></svg></div>
  <span class="feature-label">Experienced with Chinese</span>
</div>
<div class="abs feature" style="top:440px">
  <div class="feature-icon"><svg width="18" height="18" viewBox="0 0 18 18" fill="none" stroke="#f2c53d" stroke-width="1.5"><rect x="2" y="3" width="14" height="10" rx="1"/><path d="M5 6h8M5 9h5"/><circle cx="13" cy="13" r="2" fill="#f2c53d"/></svg></div>
  <span class="feature-label">Professionally licensed</span>
</div>
<div class="abs feature" style="top:488px">
  <div class="feature-icon"><svg width="18" height="18" viewBox="0 0 18 18" fill="#f2c53d" stroke="#f2c53d" stroke-width="1.2"><circle cx="9" cy="9" r="2.5"/><path d="M9 2v4M9 12v4M2 9h4M12 9h4"/><circle cx="9" cy="2" r="1"/><circle cx="9" cy="16" r="1"/><circle cx="2" cy="9" r="1"/><circle cx="16" cy="9" r="1"/></svg></div>
  <span class="feature-label">Gives Referral Fee</span>
</div>
<div class="abs notch notch-about"></div>

<h2 class="abs contact-title">CONTACT</h2>
<div class="abs field" style="top:684px">First &amp; Last name
  <svg width="16" height="16" viewBox="0 0 16 16" fill="#d0d0d0"><circle cx="8" cy="5" r="3.5"/><path d="M1 16c0-4 3-6 7-6s7 2 7 6z"/></svg></div>
<div class="abs field" style="top:721px">Phone No.
  <svg width="15" height="15" viewBox="0 0 16 16" fill="#d0d0d0"><path d="M3 1l3 3-2 2c1 2 3 4 5 5l2-2 3 3-2 3C7 15 1 9 1 3z"/></svg></div>
<div class="abs field" style="top:759px">Email Id *
  <svg width="15" height="12" viewBox="0 0 15 12" fill="none" stroke="#d0d0d0" stroke-width="1.3" style="top:6px"><rect x="1" y="1" width="13" height="10"/><path d="M1 1l6.5 5L14 1"/></svg></div>
<div class="abs message">Your message</div>
<div class="abs send">SEND MESSAGE</div>

<section class="abs connect"></section>
<div class="abs notch notch-contact"></div>
<h2 class="abs connect-title">CONNECT WITH US</h2>
<div class="abs network" style="left:95px">Vantrel</div>
<div class="abs network" style="left:164px">Orbelle</div>
<div class="abs network" style="left:232px">Quendo</div>
<div class="abs network" style="left:301px">Mirvale</div>
<div class="abs network" style="left:370px">Tazzen</div>
<div class="abs network" style="left:438px">Lunoro</div>
<div class="abs network" style="left:507px">Pekkari</div>
<div class="abs network" style="left:575px">Dravio</div>
<div class="abs network" style="left:643px">Sollet</div>
<div class="abs network" style="left:709px">Kivoro</div>

<footer class="abs footer">
  <span>© 2015 Wayfarepage.com All Rights Reserved.</span>
  <span>Terms of Service &nbsp;|&nbsp; Privacy Policy</span>
</footer>

</body>
</html>
```